Webbanner-Design für Kaffee-Abo
Zielgruppe
Kaffeeröster mit eigenem Onlineshop
Zielgruppe: Kaffeeliebhaber, die Handgerösteten Kaffee zu einem super Preis finden wollen.
Wir möchten ein Kaffee-Abo für unsere Kunden anbieten, damit Ihnen der Einkauf ihres Lieblingskaffees erleichtert wird. Den Kunden soll es nie wieder passieren, dass die Kaffeebohnen leer sind, also können sie einen eigenen Rhytmus wählen, in dem sie den Kaffee automatisch zugesandt bekommen. Es gibt keine Mindestlaufzeit und das Abo kann jederzeit gekündigt oder unterbrochen werden.
Uns ist ein persönlicher und lockerer Umgang mit unseren Kunden wichtig. Daher soll der Internetauftritt auch locker, freundlich und sympathisch wirken.
Schauen Sie bitte auf unsere Webseite:
www.bohnenwerkstatt-lind.de
Aufgabenstellung
Uns ist wichtig, dass der Banner freundlich und Sympatisch wirkt und Vertrauen vermittelt anstatt Angst vor einem verbindlichen Abo entstehen zu lassen (Unser Abo ist jederzeit unkompliziert kündbar). Der Banner sollte zu unserer Webseite passen.
Unsere Webseite ist unter www.bohnenwerkstatt-lind.de zu finden. Es wird ein neuer „Reiter“ mit dem Titel „Kaffee-Abo“ auf die Webseite implementiert werden. Hierfür möchten wir den Banner von Ihnen gestaltet haben. Der Banner sollte dem Format von unseren anderen Bannern entsprechen. Es besteht auch die Möglichkeit, dass ein 2 bis 3 Teiliger Wechselbanner (Wie auf unserer Startseite) eingebaut wird.

```html
<!DOCTYPE html>
<html lang="de">
<head>
<meta charset="utf-8">
<title>Bohnenwerkstatt – Kaffee-Abo</title>
<link rel="stylesheet" href="https://fonts.googleapis.com/css2?family=Open+Sans:wght@400;600;700&family=Permanent+Marker&display=swap">
<style>
  :root {
    --bar: #222222;
    --black: #000000;
    --white: #ffffff;
    --accent: #c9a07a;
    --muted: #d9c3ac;
  }
  * { margin: 0; padding: 0; box-sizing: border-box; }
  html, body { width: 1200px; height: 610px; overflow: hidden; background: var(--black); }
  body { font-family: "Open Sans", Arial, sans-serif; color: var(--white); position: relative; }

  .topbar { position: absolute; left: 0; top: 0; width: 1200px; height: 28px; background: var(--bar); font-size: 8.5px; }
  .topbar .item { position: absolute; top: 0; height: 28px; display: flex; align-items: center; gap: 6px; white-space: nowrap; }
  .shipping { left: 240px; }
  .phone { left: 562px; color: var(--muted); }
  .mail { left: 666px; color: var(--muted); }
  .cart { left: 830px; top: 5px !important; height: 20px !important; border: 1px solid var(--accent); border-radius: 3px; padding: 0 6px; color: var(--muted); }
  .cart .count { border-left: 1px solid var(--accent); padding-left: 6px; margin-left: 2px; }
  .user { left: 938px; }
  .icon { fill: var(--muted); }

  .header { position: absolute; left: 0; top: 28px; width: 1200px; height: 83px; background: var(--black); }
  .brand { position: absolute; left: 247px; top: 32px; display: flex; align-items: center; gap: 8px; font-size: 20px; font-weight: 400; letter-spacing: 1.5px; white-space: nowrap; }
  .brand .dot { width: 14px; height: 14px; border-radius: 50%; background: var(--white); }
  .nav { position: absolute; left: 558px; top: 55px; display: flex; gap: 20px; font-size: 11.5px; font-weight: 700; white-space: nowrap; }
  .nav .active { color: var(--accent); }

  .hero { position: absolute; left: 5px; top: 111px; width: 1190px; height: 384px; overflow: hidden; }
  .hero-photo { position: absolute; inset: 0;
    background: linear-gradient(100deg, #2e3426 0%, #3d3a30 25%, #6f6a63 42%, #c9c6c2 58%, #b4aca3 72%, #5e4a3a 90%, #4a3426 100%); }
  .hero-shade { position: absolute; inset: 0; background: linear-gradient(90deg, rgba(0,0,0,0.45) 0%, rgba(0,0,0,0.15) 55%, rgba(0,0,0,0) 100%); }
  .hero-title { position: absolute; left: 70px; top: 92px; font-family: "Permanent Marker", Impact, "Arial Black", sans-serif; font-weight: 400; font-size: 60px; line-height: 1; letter-spacing: 1px; white-space: nowrap; }
  .benefits { position: absolute; left: 72px; top: 178px; list-style: none; }
  .benefits li { display: flex; align-items: center; gap: 15px; height: 39px; font-size: 28px; white-space: nowrap; }
  .benefits svg { width: 22px; height: 22px; flex: none; }

  .claim { position: absolute; left: 0; top: 510px; width: 1200px; text-align: center; font-family: "Permanent Marker", Impact, "Arial Black", sans-serif; font-weight: 400; font-size: 31px; line-height: 49px; text-transform: uppercase; white-space: nowrap; }
</style>
</head>
<body>
  <div class="topbar">
    <div class="item shipping">
      <svg width="15" height="12" viewBox="0 0 15 12"><path fill="#fff" d="M0 1h9v7H0zM9 3h3l3 3v2H9z"/><circle cx="3" cy="9.5" r="1.8" fill="#fff"/><circle cx="11.5" cy="9.5" r="1.8" fill="#fff"/></svg>
      <span>Kostenloser Versand ab 30,00 €</span>
    </div>
    <div class="item phone">
      <svg width="13" height="13" viewBox="0 0 14 14"><rect class="icon" width="14" height="14" rx="2"/><path fill="#222" d="M4 3c1 0 1.5 1.6 1.2 2.2L4.6 6c.6 1.4 1.6 2.4 3 3l.8-.6c.6-.3 2.2.2 2.2 1.2 0 .8-.8 1.4-1.6 1.4C6 11 3 8 3 4.6 3 3.8 3.4 3 4 3z"/></svg>
      <span>+49 5471 2086514</span>
    </div>
    <div class="item mail">
      <svg width="15" height="11" viewBox="0 0 15 11"><rect class="icon" width="15" height="11" rx="1"/><path d="M1 1l6.5 5L14 1" stroke="#222" stroke-width="1.3" fill="none"/></svg>
      <span>info@bohnenwerkstatt-lind.de</span>
    </div>
    <div class="item cart">
      <svg width="14" height="12" viewBox="0 0 14 12"><path class="icon" d="M0 3h14l-1.5 8h-11zM4 3l2-3h2l2 3"/></svg>
      <span>Warenkorb</span><span class="count">0</span>
    </div>
    <div class="item user">
      <svg width="16" height="16" viewBox="0 0 16 16"><circle class="icon" cx="8" cy="8" r="8"/><circle cx="8" cy="6" r="2.6" fill="#222"/><path d="M3.5 13c1-2.4 2.6-3.3 4.5-3.3s3.5.9 4.5 3.3" fill="#222"/></svg>
    </div>
  </div>

  <header class="header">
    <div class="brand"><span class="dot"></span><span>BOHNENWERKSTATT</span></div>
    <nav class="nav">
      <span class="active">Kaffee-Shop</span>
      <span>Business-Kaffee</span>
      <span>Espressino</span>
      <span>Der Clan</span>
      <span>Kontakt</span>
    </nav>
  </header>

  <section class="hero">
    <div class="hero-photo" role="img" aria-label="Foto: Person im weißen T-Shirt hält ein Tablet und trinkt aus einer grauen Kaffeetasse"></div>
    <div class="hero-shade"></div>
    <h1 class="hero-title">KAFFEE-ABO</h1>
    <ul class="benefits">
      <li><svg viewBox="0 0 22 22"><path d="M15 3H3v16h16v-7" stroke="#fff" stroke-width="2.4" fill="none"/><path d="M7 10l4 4 9-10" stroke="#fff" stroke-width="2.4" fill="none"/></svg>keine Mindestlaufzeit</li>
      <li><svg viewBox="0 0 22 22"><path d="M15 3H3v16h16v-7" stroke="#fff" stroke-width="2.4" fill="none"/><path d="M7 10l4 4 9-10" stroke="#fff" stroke-width="2.4" fill="none"/></svg>jederzeit zu unterbrechen</li>
      <li><svg viewBox="0 0 22 22"><path d="M15 3H3v16h16v-7" stroke="#fff" stroke-width="2.4" fill="none"/><path d="M7 10l4 4 9-10" stroke="#fff" stroke-width="2.4" fill="none"/></svg>die Freude an Kaffee</li>
    </ul>
  </section>

  <h2 class="claim">Die Bohnenwerkstatt-Familie,<br>deine Kaffeerösterei!</h2>
</body>
</html>
```